Serial Entrepreneur Business Card: 4 Logo Design

I am a serial entrepreneur and a full time mechanical engineer. I have four businesses. I would like to display them all on one business card.
*Please see the attached PDF for the design requirements*

www.KelbroNest.com

Businesses
-KelbroNest
-Quiet Lantern Properties
-Torlen Products
-Drosk Harbor Cast

Target Market(s)

Clients, Entrepreneurs, Associates, really anyone. Should be very professional.

Industry/Entity Type

Entrepreneur

Contact Information for Business Card

3.5" x 2" Standard Business Card Size
** Please review the attached requirement PDF for in depth detail on what I am expecting**

Font styles to use
Sans Serif

Requirements
Must have
• My personal contact information:
• First Name: Dae hwan
• Last Name: Pellow
• Nick Name: Riko
• Address: 83 Tolmer Court, Garfield NJ 07392
• Phone Number: 201-574-2916
• Email: RikodPellow@mailnest.example
• Website: www.KelbroNest.com
• All Four Logos of the Companies I own:
• -KelbroNest
• -Quiet Lantern Properties
• -Torlen Products
• -Drosk Harbor Cast
• My Professions:
• -Prototyping Engineer
• -Real Estate Investor
• -Financial Blogger
• -Video Podcaster
• -Online Retail Seller
Nice to have
• If it fits, please include the website for each logo, if there is more space please include the email for each.
• It might be nice to have the QX GUILD Logo, or TOVRA logo for my full-time job. But only if it fits.

```html
<!DOCTYPE html>
<html lang="en">
<head>
<meta charset="utf-8">
<title>Dae hwan Pellow — Business Card</title>
<link rel="stylesheet" href="https://fonts.googleapis.com/css2?family=Open+Sans:wght@400;600;700;800&display=swap">
<style>
  :root {
    --backdrop: #e9e6e1;
    --card-white: #ffffff;
    --brand-green: #118a16;
    --brand-green-deep: #0b7410;
    --pattern-tint: #eef5ee;
    --ink: #1b1b1b;
    --ink-soft: #555555;
    --paper-text: #ffffff;
  }
  * { box-sizing: border-box; margin: 0; padding: 0; }
  html, body {
    width: 1200px; height: 987px; overflow: hidden;
    background: var(--backdrop);
    font-family: "Open Sans", sans-serif;
  }
  .canvas { position: relative; width: 1200px; height: 987px; }

  .card {
    position: absolute; left: 293px; width: 615px;
    border-radius: 21px; overflow: hidden;
    box-shadow: 0 4px 14px rgba(0,0,0,.25);
  }
  .card-front { top: 130px; height: 352px; background: var(--card-white); }
  .card-back { top: 506px; height: 351px; background: var(--brand-green); }

  .pattern-field { position: absolute; inset: 0; }
  .card-front .pattern-field { background: linear-gradient(180deg, var(--pattern-tint), #f7faf7 50%, var(--pattern-tint)); }
  .card-back .pattern-field { background: linear-gradient(180deg, #15911a, var(--brand-green-deep)); }

  .venture {
    position: absolute; width: 290px; transform: translateX(-50%);
    display: flex; flex-direction: column; align-items: center; text-align: center;
  }
  .venture-mark { display: flex; align-items: center; gap: 9px; height: 40px; }
  .venture-square { width: 26px; height: 26px; background: var(--brand-green); flex: none; }
  .venture-name { font-weight: 800; font-size: 27px; color: var(--ink); line-height: 1; white-space: nowrap; }
  .venture-name.green { color: var(--brand-green); }
  .venture-name.compact { font-size: 20px; }
  .venture-url { margin-top: 4px; font-size: 11px; letter-spacing: 2px; color: var(--ink-soft); white-space: nowrap; }
  .v-kelbro { left: 162px; top: 136px; }
  .v-torlen { left: 448px; top: 136px; }
  .v-lantern { left: 164px; top: 260px; }
  .v-drosk { left: 448px; top: 258px; }

  .owner { position: absolute; left: 55px; top: 64px; color: var(--paper-text); }
  .owner-name { font-weight: 700; font-size: 23px; line-height: 28px; letter-spacing: .3px; }
  .owner-roles { list-style: none; margin-top: 1px; font-size: 15px; line-height: 21.5px; }
  .divider { position: absolute; left: 55px; right: 46px; top: 211px; height: 1px; background: rgba(255,255,255,.85); }
  .contact { position: absolute; left: 55px; top: 223px; list-style: none; color: var(--paper-text); font-size: 15px; line-height: 23.5px; }
  .contact li { display: flex; align-items: center; gap: 8px; white-space: nowrap; }
  .contact svg { width: 14px; height: 14px; fill: var(--paper-text); flex: none; }
  .address { position: absolute; right: 49px; top: 252px; text-align: right; color: var(--paper-text); font-size: 15px; line-height: 22px; font-style: normal; }
</style>
</head>
<body>
<main class="canvas">
  <section class="card card-front" aria-label="Card front with four ventures">
    <div class="pattern-field" role="img" aria-label="Faint repeating pattern of venture symbols"></div>
    <div class="venture v-kelbro">
      <div class="venture-mark"><span class="venture-square"></span><span class="venture-name">KelbroNest</span></div>
      <div class="venture-url">www.KelbroNest.com</div>
    </div>
    <div class="venture v-torlen">
      <div class="venture-mark"><span class="venture-name">Torlen Products</span></div>
      <div class="venture-url">www.torlen.com</div>
    </div>
    <div class="venture v-lantern">
      <div class="venture-mark"><span class="venture-name compact">Quiet Lantern Properties</span></div>
      <div class="venture-url">www.quietlantern.com</div>
    </div>
    <div class="venture v-drosk">
      <div class="venture-mark"><span class="venture-square"></span><span class="venture-name compact green">Drosk Harbor Cast</span></div>
      <div class="venture-url">www.droskharborcast.com</div>
    </div>
  </section>

  <section class="card card-back" aria-label="Card back with contact details">
    <div class="pattern-field" role="img" aria-label="Subtle repeating pattern of venture symbols on green"></div>
    <div class="owner">
      <h1 class="owner-name">DAE HWAN PELLOW</h1>
      <ul class="owner-roles">
        <li>Prototyping Engineer</li>
        <li>Real Estate Investor</li>
        <li>Financial Blogger</li>
        <li>Video Podcaster</li>
        <li>Online Retail Seller</li>
      </ul>
    </div>
    <div class="divider"></div>
    <ul class="contact">
      <li><svg viewBox="0 0 24 24"><path d="M6.6 10.8a15.1 15.1 0 0 0 6.6 6.6l2.2-2.2c.3-.3.7-.4 1-.2 1.1.4 2.3.6 3.6.6.6 0 1 .4 1 1V20c0 .6-.4 1-1 1A17 17 0 0 1 3 4c0-.6.4-1 1-1h3.5c.6 0 1 .4 1 1 0 1.3.2 2.5.6 3.6.1.3 0 .7-.2 1z"/></svg>201-574-2916</li>
      <li><svg viewBox="0 0 24 24"><path d="M2 5h20v14H2zm2 2v.5l8 5 8-5V7z"/></svg>RikodPellow@mailnest.example</li>
      <li><svg viewBox="0 0 24 24"><circle cx="12" cy="12" r="10"/></svg>www.KelbroNest.com</li>
    </ul>
    <address class="address">83 Tolmer Court<br>Garfield NJ 07392</address>
  </section>
</main>
</body>
</html>
```